Bref créative
Quillmont Care Associates
Business Cards & Stationary
Bright & Fun-filled
Harold J. Mabbery, Ph.D.
Co-founder
4815 North Larkin Road
Marrowick, CA 90417
drhmabbery@examplemail.net
Licensed Psychologist PSY58706
On the front of the card, we would like to see some versions with the logos symbol.
This business card is for a California Board Licensed Psychologist.
The look of this should be professional, but because it is for therapy, we would like it to be professional with a hint of:
* warm and welcoming
* serenity, tranquility and happiness
* positive, future, growth
On the back of the business card please place the:
1. Logo symbol and company name
2. Child, Adolescence, Family, Adult Therapy
logo
We need to see how the back of a card looks with the Quillmont Care Logo and the following information attached.

```html
<!DOCTYPE html>
<html lang="en">
<head>
<meta charset="utf-8">
<title>Quillmont Care Associates – Business Card</title>
<link rel="stylesheet" href="https://fonts.googleapis.com/css2?family=Lora:wght@400;700&display=swap">
<style>
  :root {
    --backdrop: #2b2b2d;
    --card: #ffffff;
    --card-shade: #eef1f3;
    --brand-blue: #1f7fc1;
    --brand-teal: #6cc3cf;
    --soft-teal: #bfe4ea;
    --ink: #4a4f55;
    --muted: #7b8a93;
  }
  * { box-sizing: border-box; margin: 0; padding: 0; }
  html, body { width: 1200px; height: 901px; overflow: hidden; }
  body {
    background: var(--backdrop);
    font-family: "Lora", Georgia, serif;
    display: flex; flex-direction: column; align-items: center; justify-content: center;
    gap: 30px;
  }
  .card {
    position: relative;
    width: 720px; height: 411px;
    background: linear-gradient(135deg, var(--card) 60%, var(--card-shade));
    overflow: hidden;
    box-shadow: 0 10px 30px rgba(0,0,0,.45);
  }
  .brand-dot { width: 40px; height: 40px; border-radius: 50%; background: var(--brand-teal); flex: none; }
  .brand-name { font-weight: 700; color: var(--brand-blue); line-height: 1.1; white-space: nowrap; }

  /* back side */
  .card-back { display: flex; flex-direction: column; align-items: center; justify-content: center; gap: 16px; }
  .card-back .brand-dot { width: 64px; height: 64px; }
  .card-back .brand-name { font-size: 28px; letter-spacing: .5px; }
  .services { font-size: 16px; color: var(--ink); letter-spacing: .3px; }

  /* front side */
  .details { position: absolute; left: 44px; top: 40px; width: 400px; }
  .details .brand { display: flex; flex-direction: column; align-items: flex-start; gap: 10px; }
  .details .brand-dot { margin-left: 60px; }
  .details .brand-name { font-size: 25px; letter-spacing: .4px; }
  .person { margin-top: 18px; font-size: 20px; font-weight: 700; color: var(--brand-blue); }
  .role { font-size: 15px; color: var(--muted); margin-top: 4px; }
  .address { margin-top: 16px; font-size: 14.5px; color: var(--ink); line-height: 1.45; font-style: normal; }
  .contacts { list-style: none; margin-top: 10px; font-size: 14.5px; color: var(--ink); }
  .contacts li { display: flex; align-items: center; gap: 10px; line-height: 1.75; }
  .contacts svg { width: 15px; height: 15px; fill: var(--brand-blue); flex: none; }
  .halo {
    position: absolute; right: -120px; top: -30px;
    width: 470px; height: 470px; border-radius: 50%;
    background: radial-gradient(circle at 40% 40%, var(--soft-teal), var(--brand-teal) 65%, var(--brand-blue));
    opacity: .85;
  }
</style>
</head>
<body>
  <section class="card card-back">
    <span class="brand-dot"></span>
    <span class="brand-name">Quillmont Care Associates</span>
    <p class="services">Child, Adolescence, Family, Adult Therapy</p>
  </section>

  <section class="card card-front">
    <div class="halo" role="img" aria-label="Large soft brand circle decoration"></div>
    <div class="details">
      <div class="brand">
        <span class="brand-dot"></span>
        <span class="brand-name">Quillmont Care Associates</span>
      </div>
      <p class="person">Harold J. Mabbery, Ph.D.</p>
      <p class="role">Co-founder</p>
      <address class="address">4815 North Larkin Road<br>Marrowick, CA 90417</address>
      <ul class="contacts">
        <li><svg viewBox="0 0 24 24"><path d="M6.6 10.8a15 15 0 0 0 6.6 6.6l2.2-2.2a1 1 0 0 1 1-.25 11.4 11.4 0 0 0 3.6.57 1 1 0 0 1 1 1V20a1 1 0 0 1-1 1A17 17 0 0 1 3 4a1 1 0 0 1 1-1h3.5a1 1 0 0 1 1 1c0 1.25.2 2.450.57 3.57a1 1 0 0 1-.25 1z"/></svg>(555) 014-2273</li>
        <li><svg viewBox="0 0 24 24"><path d="M6 3h12v5H6zM4 9h16a2 2 0 0 1 2 2v6h-4v4H6v-4H2v-6a2 2 0 0 1 2-2zm4 7v3h8v-3z"/></svg>(555) 014-8810</li>
        <li><svg viewBox="0 0 24 24"><path d="M2 5h20v14H2zm2 2v.5l8 5 8-5V7zm0 2.8V17h16V9.8l-8 5z"/></svg>drhmabbery@examplemail.net</li>
      </ul>
    </div>
  </section>
</body>
</html>
```